Yard Sign Design Needed

Yard sign needed for mowing & landscaping company. Would like to use the top logo with black background which is attached. Would like MOWING to be in large standout letters. The word "landscaping" can be smaller and more artistic or omitted. Will need room for phone number once design is approved. The phone number will need to stand out and look identical/similar to the word 'MOWING"

```html
<!DOCTYPE html>
<html lang="en">
<head>
<meta charset="utf-8">
<title>Brantley Groundworks – Mowing Yard Sign</title>
<link rel="stylesheet" href="https://fonts.googleapis.com/css2?family=Exo+2:wght@300;600;800&display=swap">
<style>
  :root {
    --sign-black: #050505;
    --leaf-green: #8fb33a;
    --leaf-bright: #a6d234;
    --leaf-deep: #5f7a2a;
    --stripe-white: #f2f5ea;
    --accent-yellow: #e4ea2c;
    --ink: #0a0a0a;
    --paper: #ffffff;
  }
  html, body {
    margin: 0;
    padding: 0;
    width: 1200px;
    height: 894px;
    overflow: hidden;
    background: var(--paper);
  }
  .yard-sign {
    position: relative;
    width: 1200px;
    height: 894px;
    background: var(--sign-black);
    overflow: hidden;
    font-family: "Exo 2", sans-serif;
  }
  .chevron-bands {
    position: absolute;
    inset: 0;
    width: 1200px;
    height: 894px;
  }
  .brand {
    position: absolute;
    top: 150px;
    left: 0;
    width: 1120px;
    text-align: center;
  }
  .brand-mark {
    width: 70px;
    height: 70px;
    margin: 0 auto 34px;
    background: var(--leaf-green);
  }
  .brand-name {
    margin: 0;
    color: var(--leaf-green);
    font-weight: 600;
    font-size: 44px;
    line-height: 1.08;
    letter-spacing: 1px;
    text-transform: uppercase;
  }
  .service-title {
    position: absolute;
    top: 575px;
    left: 0;
    width: 1120px;
    margin: 0;
    text-align: center;
    color: var(--paper);
    font-weight: 800;
    font-size: 124px;
    line-height: 1;
    letter-spacing: 4px;
  }
  .service-subtitle {
    position: absolute;
    top: 702px;
    left: 108px;
    width: 910px;
    margin: 0;
    display: flex;
    justify-content: space-between;
    color: var(--accent-yellow);
    font-weight: 300;
    font-size: 40px;
    line-height: 1;
  }
  .phone-number {
    position: absolute;
    top: 738px;
    left: 0;
    width: 1080px;
    margin: 0;
    text-align: center;
    color: var(--ink);
    font-weight: 800;
    font-size: 104px;
    line-height: 1;
    letter-spacing: 2px;
  }
</style>
</head>
<body>
  <main class="yard-sign">
    <svg class="chevron-bands" viewBox="0 0 1200 894" aria-hidden="true">
      <defs>
        <radialGradient id="greenField" cx="0.47" cy="0.72" r="0.65">
          <stop offset="0" stop-color="var(--leaf-bright)"/>
          <stop offset="0.55" stop-color="var(--leaf-green)"/>
          <stop offset="1" stop-color="var(--leaf-deep)"/>
        </radialGradient>
        <linearGradient id="stripeLeft" x1="0" x2="1" y1="0" y2="0">
          <stop offset="0" stop-color="var(--stripe-white)"/>
          <stop offset="0.6" stop-color="var(--leaf-bright)"/>
          <stop offset="1" stop-color="#55602f"/>
        </linearGradient>
        <linearGradient id="stripeRight" x1="0" x2="1" y1="0" y2="0">
          <stop offset="0" stop-color="var(--leaf-green)"/>
          <stop offset="1" stop-color="var(--stripe-white)"/>
        </linearGradient>
      </defs>
      <polygon points="0,420 560,590 1200,460 1200,894 0,894" fill="url(#greenField)"/>
      <polygon points="0,355 560,520 560,545 0,380" fill="url(#stripeLeft)"/>
      <polygon points="560,520 1200,390 1200,408 560,545" fill="#2a2a2a"/>
      <polygon points="0,418 560,580 560,600 0,438" fill="var(--leaf-bright)" opacity="0.85"/>
      <polygon points="560,580 1200,438 1200,462 560,600" fill="url(#stripeRight)"/>
    </svg>

    <header class="brand">
      <div class="brand-mark"></div>
      <p class="brand-name">Brantley<br>Groundworks LLC</p>
    </header>

    <h1 class="service-title">MOWING</h1>
    <p class="service-subtitle" aria-label="landscaping">
      <span>l</span><span>a</span><span>n</span><span>d</span><span>s</span><span>c</span><span>a</span><span>p</span><span>i</span><span>n</span><span>g</span>
    </p>
    <p class="phone-number">05550142876</p>
  </main>
</body>
</html>
```